Template design for organic gardening site for ShopVantra platform

We need a template design for our new 'Fen Leaf Naturals' shopvantra site. Fen Leaf Naturals specialises in organic nutrients for gardening plus all equipment needed to grow.
Domain name will be www.fenleafnaturals.co.uk
Colours used should include logo colours, see attached image. Other colours to compliment the greens and lift the feel of the site could be yellow or orange.
Home page design should include, but not limited to the following:
Interactive banner carousel space
A smaller banner advertising space
Featured products
New products
Sale products feature/link
Articles links/feature
+ all standard shopvantra features such as menus, etc
The site will be selling products (these are nutrients) such as:
Pelvarimost
Marsh hare soil tonic
Terrawix
Nuro pods
Stem triumph
Sprout charm
Vel
Flint amber
Moswelder
+ more products and brands
Site layouts we like include:
www.tidemarkaquafarm.co.uk ... A bit old fashioned but cool
www.lanternbeds.co.uk ... Nice but too compact
www.flintamber.com ... Has a nice top half
www.sponsorapod.org.uk ... Nice colours and header
www.penhurstplants.co.uk ... nice layout, but needs image carousel
www.wrenmeal.co.uk ... Nice background and colours
www.thistle.co.uk ... Nice colours and layout
www.danielmorrowhorticulture.com ... Nice layout and header
www.sprivant.co.uk ... Cool colours and shop pages layout is nice
www.aquavenor.co.uk ... One of the best layouts
The site should feel clean, modern and elegant.
Target Market(s)
Indoor and outdoor organic gardeners
Look and feel

```html
<!DOCTYPE html>
<html lang="en">
<head>
<meta charset="utf-8">
<title>Fen Leaf Naturals – Home</title>
<link href="https://fonts.googleapis.com/css2?family=Open+Sans:wght@400;600;700;800&display=swap" rel="stylesheet">
<style>
  :root{
    --green:#6ab344;
    --green-dark:#3f7a35;
    --green-deep:#2f5f2a;
    --grey-band:#eef0ec;
    --grey-line:#dcdfd9;
    --grey-box:#d9d9d9;
    --text:#4a4a4a;
    --muted:#8a8f86;
    --white:#ffffff;
    --soil-1:#3a2c22;
    --soil-2:#6b5444;
  }
  *{box-sizing:border-box;margin:0;padding:0}
  html,body{width:1200px;height:800px;overflow:hidden;background:var(--white)}
  body{font-family:"Open Sans",Arial,sans-serif;color:var(--text)}
  .site{position:relative;width:790px;margin:0 auto;padding-top:40px}

  /* header */
  .site-header{display:flex;justify-content:space-between;align-items:flex-start;height:110px}
  .brand{display:flex;align-items:center;gap:12px;margin-top:10px}
  .brand-mark{width:58px;height:58px;background:var(--green)}
  .brand-name{font-weight:800;font-size:30px;line-height:1;color:var(--green-dark);text-transform:uppercase;width:210px}
  .header-tools{display:flex;flex-direction:column;align-items:flex-end;gap:14px;margin-top:52px}
  .search{display:flex}
  .search-field{width:150px;height:24px;border:1px solid var(--grey-line);border-right:none}
  .search-btn{width:24px;height:24px;background:var(--green);display:flex;align-items:center;justify-content:center}
  .cart{display:flex;gap:8px;align-items:flex-start;font-size:10px;color:var(--text);border:1px solid var(--grey-line);padding:5px 8px}
  .cart-links{line-height:1.35}

  /* nav */
  .main-nav{display:flex;gap:24px;background:var(--grey-band);height:26px;align-items:center;padding:0 14px;font-size:11px;font-weight:600;color:var(--green-deep);margin-top:6px}
  .main-nav span::after{content:" ▾";font-size:8px;color:var(--muted)}

  /* hero row */
  .hero-row{display:flex;gap:16px;margin-top:18px;height:258px}
  .shop-for{width:180px;border:1px solid var(--grey-line)}
  .panel-title{background:var(--green-dark);color:var(--white);font-size:13px;font-weight:700;padding:8px 12px}
  .shop-for ul{list-style:none;padding:8px 12px}
  .shop-for li{font-size:11px;color:var(--muted);padding:5px 0;border-bottom:1px solid var(--grey-band)}
  .carousel{position:relative;width:445px;height:258px;background:linear-gradient(160deg,#9fd66b 0%,#5fae3a 45%,#2f7a28 100%);color:var(--white)}
  .carousel-copy{position:absolute;left:22px;top:26px}
  .carousel-offer{font-size:30px;font-weight:700;line-height:1.1}
  .carousel-sub{font-size:26px;font-weight:400;line-height:1.2}
  .shop-now{position:absolute;left:22px;bottom:26px;background:var(--green);color:var(--white);font-size:12px;font-weight:700;padding:8px 20px}
  .arrow{position:absolute;top:116px}
  .arrow-prev{left:8px}.arrow-next{right:8px}
  .dots{position:absolute;bottom:12px;left:50%;transform:translateX(-50%);display:flex;gap:5px}
  .dots i{width:6px;height:6px;border-radius:50%;background:rgba(255,255,255,.6)}
  .dots i:first-child{background:var(--white)}
  .side-ads{width:133px;display:flex;flex-direction:column;gap:10px}
  .promo{background:var(--green);color:var(--white);height:148px;padding:24px 10px 10px;font-size:10px;text-align:center;display:flex;flex-direction:column;justify-content:space-between}
  .promo-link{text-align:left;font-size:9px}
  .ad-slot{background:var(--grey-box);height:75px}

  /* featured */
  .section-bar{background:var(--green-dark);color:var(--white);font-size:13px;font-weight:700;padding:8px 14px;margin-top:16px}
  .product-grid{display:grid;grid-template-columns:repeat(4,190px);justify-content:space-between;margin-top:18px;row-gap:18px}
  .product-card{border:1px solid var(--grey-line);padding:10px;height:270px}
  .product-image{height:160px;background:radial-gradient(circle at 50% 65%,#c79a7f 0%,var(--soil-2) 35%,var(--soil-1) 80%)}
  .product-name{font-size:11px;color:var(--muted);margin-top:10px}
  .product-price{font-size:15px;font-weight:700;color:var(--text);margin-top:4px}
  .add-to-cart{display:inline-block;margin-top:12px;background:var(--green);color:var(--white);font-size:10px;font-weight:700;padding:5px 10px}
</style>
</head>
<body>
<div class="site">
  <header class="site-header">
    <div class="brand">
      <div class="brand-mark"></div>
      <div class="brand-name">Fen Leaf Naturals</div>
    </div>
    <div class="header-tools">
      <div class="search">
        <div class="search-field"></div>
        <div class="search-btn">
          <svg width="12" height="12" viewBox="0 0 12 12"><circle cx="5" cy="5" r="3.5" fill="none" stroke="#fff" stroke-width="1.5"/><line x1="7.6" y1="7.6" x2="11" y2="11" stroke="#fff" stroke-width="1.5"/></svg>
        </div>
      </div>
      <div class="cart">
        <svg width="18" height="14" viewBox="0 0 18 14"><path d="M1 1h3l2 8h9l2-6H5" fill="none" stroke="#3f7a35" stroke-width="1.5"/><circle cx="7" cy="12" r="1.3" fill="#3f7a35"/><circle cx="14" cy="12" r="1.3" fill="#3f7a35"/></svg>
        <div class="cart-links"><div>Cart 0 items</div><div>Checkout</div><div>Wishlist</div></div>
      </div>
    </div>
  </header>

  <nav class="main-nav">
    <span>Plants</span><span>Garden Care</span><span>Landscaping</span><span>Why Us</span><span>Tour</span><span>Blog</span><span>Customer Services</span>
  </nav>

  <section class="hero-row">
    <aside class="shop-for">
      <div class="panel-title">Shop For</div>
      <ul>
        <li>Organic Product</li><li>Organic Product</li><li>Organic Product</li><li>Organic Product</li>
        <li>Organic Product</li><li>Organic Product</li><li>Organic Product</li><li>Organic Product</li>
      </ul>
    </aside>
    <div class="carousel" role="img" aria-label="Banner photo of leafy green lettuce plants growing">
      <div class="carousel-copy">
        <div class="carousel-offer">25 % Off</div>
        <div class="carousel-sub">Organic Product</div>
      </div>
      <div class="shop-now">Shop Now</div>
      <svg class="arrow arrow-prev" width="10" height="16" viewBox="0 0 10 16"><path d="M8 2L2 8l6 6" fill="none" stroke="#fff" stroke-width="2"/></svg>
      <svg class="arrow arrow-next" width="10" height="16" viewBox="0 0 10 16"><path d="M2 2l6 6-6 6" fill="none" stroke="#fff" stroke-width="2"/></svg>
      <div class="dots"><i></i><i></i><i></i><i></i><i></i></div>
    </div>
    <div class="side-ads">
      <div class="promo">
        <div>See our incredible range of Nutrients</div>
        <div class="promo-link">Shop Now</div>
      </div>
      <div class="ad-slot"></div>
    </div>
  </section>

  <div class="section-bar">Featured Products</div>
  <section class="product-grid">
    <article class="product-card"><div class="product-image" role="img" aria-label="Hands holding rich organic soil"></div><div class="product-name">Organic Product</div><div class="product-price">$50</div><div class="add-to-cart">Add to Cart</div></article>
    <article class="product-card"><div class="product-image" role="img" aria-label="Hands holding rich organic soil"></div><div class="product-name">Organic Product</div><div class="product-price">$50</div><div class="add-to-cart">Add to Cart</div></article>
    <article class="product-card"><div class="product-image" role="img" aria-label="Hands holding rich organic soil"></div><div class="product-name">Organic Product</div><div class="product-price">$50</div><div class="add-to-cart">Add to Cart</div></article>
    <article class="product-card"><div class="product-image" role="img" aria-label="Hands holding rich organic soil"></div><div class="product-name">Organic Product</div><div class="product-price">$50</div><div class="add-to-cart">Add to Cart</div></article>
    <article class="product-card"><div class="product-image" role="img" aria-label="Hands holding rich organic soil"></div></article>
    <article class="product-card"><div class="product-image" role="img" aria-label="Hands holding rich organic soil"></div></article>
    <article class="product-card"><div class="product-image" role="img" aria-label="Hands holding rich organic soil"></div></article>
    <article class="product-card"><div class="product-image" role="img" aria-label="Hands holding rich organic soil"></div></article>
  </section>
</div>
</body>
</html>
```